RW Business Card Design

My company provides advising/training and coaching services to business owners who want better financial results and better work/life balance. We help them through creating custom plans supported with education, strategic thinking and accountability.

We also help through some online courses which are geared to smaller businesses.
Updates

please also include our nth american contact # +1 555 208 4471

Industry/Entity Type

Financial

Contact Information for Business Card

Morgan Halberd
morgan@morganhalberd-example.com
+61 400 555 917
www.morganhalberd-example.com

```html
<!DOCTYPE html>
<html lang="en">
<head>
<meta charset="utf-8">
<title>RW Business Card Design</title>
<link rel="stylesheet" href="https://fonts.googleapis.com/css2?family=Didact+Gothic&family=Open+Sans:wght@400;600&display=swap">
<style>
  :root {
    --backdrop: #d8d3cb;
    --card-dark: #0c0d0f;
    --card-mid: #2a2c30;
    --card-light: #4a4d52;
    --accent: #29a9e0;
    --ink: #e8e9eb;
    --ink-soft: #a9adb3;
    --placeholder-a: #d9dbde;
    --placeholder-b: #8e9298;
  }
  * { box-sizing: border-box; margin: 0; padding: 0; }
  html, body { width: 1200px; height: 1023px; overflow: hidden; }
  body { background: var(--backdrop); position: relative; font-family: "Open Sans", sans-serif; }

  .card {
    position: absolute;
    width: 560px; height: 320px;
    border-radius: 6px;
    overflow: hidden;
    box-shadow: 0 10px 30px rgba(0,0,0,.25);
  }
  .card--front { left: 20px; top: 352px; background: linear-gradient(160deg, var(--card-light) 0%, var(--card-mid) 45%, var(--card-dark) 100%); }
  .card--back  { left: 620px; top: 352px; background: linear-gradient(200deg, var(--card-light) 0%, var(--card-mid) 50%, var(--card-dark) 100%); }

  .card__art { position: absolute; inset: 0; }

  .name {
    position: absolute;
    font-family: "Didact Gothic", sans-serif;
    text-transform: uppercase;
    letter-spacing: .5px;
    color: var(--ink);
    white-space: nowrap;
  }
  .name__first { color: var(--accent); }
  .card--front .name { left: 24px; top: 26px; font-size: 29px; }

  .contacts { position: absolute; left: 26px; top: 78px; list-style: none; }
  .contacts li {
    display: flex; align-items: center; gap: 8px;
    font-size: 11px; line-height: 20px; color: var(--ink-soft);
  }
  .contacts .icon {
    width: 12px; height: 12px; border-radius: 2px;
    background: var(--accent);
    display: flex; align-items: center; justify-content: center;
  }
  .contacts .icon svg { width: 8px; height: 8px; fill: var(--card-dark); }

  .portrait {
    position: absolute; left: 24px; bottom: 0;
    width: 150px; height: 125px;
    background: linear-gradient(180deg, var(--placeholder-a), var(--placeholder-b));
    border-radius: 4px 4px 0 0;
  }

  .brand {
    position: absolute; left: 440px; top: 62px;
    font-family: "Didact Gothic", sans-serif;
    font-size: 40px; color: var(--ink); letter-spacing: 2px;
  }

  .formula text {
    font-family: "Open Sans", sans-serif; font-weight: 600;
    font-size: 11px; fill: var(--accent); letter-spacing: .5px;
  }

  .card--back .name { left: 34px; top: 120px; font-size: 32px; }
  .tagline {
    position: absolute; right: 34px; top: 40px;
    font-family: "Didact Gothic", sans-serif;
    font-size: 30px; color: var(--ink); letter-spacing: 1px;
  }
  .goals { position: absolute; left: 36px; top: 176px; list-style: none; }
  .goals li { font-size: 13px; line-height: 22px; color: var(--ink-soft); }
</style>
</head>
<body>

<section class="card card--front" aria-label="Card front">
  <svg class="card__art" viewBox="0 0 560 320" aria-hidden="true">
    <circle cx="470" cy="90" r="175" fill="#050607"/>
    <path d="M 295.5 119.6 A 175 175 0 0 0 470 265" fill="none" stroke="#29a9e0" stroke-width="12"/>
    <path d="M 470 265 A 175 175 0 0 0 593.7 213.7" fill="none" stroke="#29a9e0" stroke-width="12"/>
  </svg>

  <h1 class="name"><span class="name__first">Morgan</span>Halberd</h1>

  <ul class="contacts">
    <li><span class="icon"><svg viewBox="0 0 10 10"><path d="M2 1h2l1 2-1.2 1a5 5 0 0 0 2.2 2.2L7 5l2 1v2a1 1 0 0 1-1 1A7 7 0 0 1 1 2a1 1 0 0 1 1-1z"/></svg></span>+61 400 555 917 (AUS)</li>
    <li><span class="icon"><svg viewBox="0 0 10 10"><path d="M2 1h2l1 2-1.2 1a5 5 0 0 0 2.2 2.2L7 5l2 1v2a1 1 0 0 1-1 1A7 7 0 0 1 1 2a1 1 0 0 1 1-1z"/></svg></span>+1 555 208 4471 (USA)</li>
    <li><span class="icon"><svg viewBox="0 0 10 10"><path d="M1 2h8v6H1z M1 2l4 3 4-3" fill="none" stroke="#0c0d0f" stroke-width="1.2"/></svg></span>morgan@morganhalberd-example.com</li>
    <li><span class="icon"><svg viewBox="0 0 10 10"><circle cx="5" cy="5" r="3.8" fill="none" stroke="#0c0d0f" stroke-width="1.1"/><path d="M1.2 5h7.6M5 1.2v7.6" stroke="#0c0d0f" stroke-width="1"/></svg></span>www.morganhalberd-example.com</li>
  </ul>

  <div class="portrait" role="img" aria-label="Illustrated portrait of the adviser"></div>

  <div class="brand">RW</div>

  <svg class="card__art formula" viewBox="0 0 560 320" aria-label="Knowledge plus planning times action equals success">
    <g stroke="#29a9e0" stroke-width="1.2" fill="none">
      <line x1="306" y1="150" x2="225" y2="286"/>
      <line x1="346" y1="214" x2="310" y2="286"/>
      <line x1="404" y1="252" x2="395" y2="286"/>
      <line x1="464" y1="265" x2="480" y2="286"/>
      <circle cx="306" cy="150" r="10"/><circle cx="346" cy="214" r="10"/>
      <circle cx="404" cy="252" r="10"/><circle cx="464" cy="265" r="10"/>
    </g>
    <g fill="#29a9e0">
      <circle cx="306" cy="150" r="6"/><circle cx="346" cy="214" r="6"/>
      <circle cx="404" cy="252" r="6"/><circle cx="464" cy="265" r="6"/>
    </g>
    <text x="225" y="302" text-anchor="middle">KNOWLEDGE</text>
    <text x="268" y="302" text-anchor="middle">+</text>
    <text x="310" y="302" text-anchor="middle">PLANNING</text>
    <text x="352" y="302" text-anchor="middle">×</text>
    <text x="395" y="302" text-anchor="middle">ACTION</text>
    <text x="437" y="302" text-anchor="middle">=</text>
    <text x="480" y="302" text-anchor="middle">SUCCESS</text>
  </svg>
</section>

<section class="card card--back" aria-label="Card back">
  <p class="tagline">I WANT TO...</p>
  <h2 class="name"><span class="name__first">Morgan</span>Halberd</h2>
  <ul class="goals">
    <li>Generate more cash...</li>
    <li>Know how to hire right the first time...</li>
    <li>Have more free time to do what I want...</li>
    <li>Have a solid plan to exit out of my business...</li>
  </ul>
</section>

</body>
</html>
```